Pull Up Sign for Financial Services Business

Looking to design a pull-up retractable banner for events. A design which I could add a second banner to so something that could flow across more than one banner would be ideal.

I have included my logo and business card so you can get an idea of colours and our branding style.

A disability image will be required on the banner. Dimensions are in image attached.

Target Market(s)

KPTA (Disability) Participants

Industry/Entity Type

Disability/Finance

Other font styles liked:
• Raleway

Requirements
Must have
• Disability Image - match our branding. Text in image uploaded

```html
<!DOCTYPE html>
<html lang="en">
<head>
<meta charset="utf-8">
<title>Harbour Plan Partners – Pull Up Banner</title>
<link href="https://fonts.googleapis.com/css2?family=Montserrat:wght@500;600;700&display=swap" rel="stylesheet">
<style>
  :root {
    --teal: #12837f;
    --teal-dark: #0c6e6b;
    --magenta: #b1306d;
    --ink: #2a2a35;
    --white: #ffffff;
    --mist: #e4f1f2;
    --stage: #e9ebec;
  }
  * { margin: 0; padding: 0; box-sizing: border-box; }
  html, body { width: 1200px; height: 1200px; overflow: hidden; background: var(--stage); }
  body { font-family: "Montserrat", Arial, sans-serif; position: relative; }

  .banner-frame {
    position: absolute; left: 369px; top: 40px;
    width: 462px; height: 1120px;
    box-shadow: 0 6px 24px rgba(0,0,0,.18);
    overflow: hidden;
  }
  .banner {
    position: absolute; left: 0; top: 0;
    width: 725px; height: 1757px;
    transform: scale(0.6372); transform-origin: 0 0;
  }
  .banner-shapes { position: absolute; inset: 0; width: 725px; height: 1757px; }

  .brand { position: absolute; left: 40px; top: 36px; width: 270px; text-align: center; }
  .brand-mark { display: block; width: 104px; height: 104px; margin: 0 auto 18px; background: var(--teal); }
  .brand-name { color: var(--teal); font-weight: 600; font-size: 30px; line-height: 1.15; letter-spacing: 1px; }

  .brand-divider { position: absolute; left: 350px; top: 36px; width: 2px; height: 190px; background: var(--ink); }

  .headline {
    position: absolute; left: 374px; top: 78px;
    font-weight: 700; font-size: 52px; line-height: 1; letter-spacing: 2px; color: var(--teal);
  }
  .headline span { color: var(--magenta); }
  .headline div + div { margin-top: 2px; }

  .pill {
    position: absolute; background: var(--white); color: var(--magenta);
    font-weight: 600; border-radius: 24px; white-space: nowrap;
  }
  .pill--coverage { left: 24px; top: 1017px; height: 43px; padding: 0 18px; font-size: 24px; line-height: 43px; letter-spacing: .6px; }
  .pill--contact { left: 24px; top: 1487px; height: 42px; padding: 0 18px; font-size: 23px; line-height: 42px; letter-spacing: .6px; background: var(--magenta); color: var(--white); }

  .benefits { position: absolute; left: 28px; top: 1078px; list-style: none; }
  .benefits li {
    display: flex; align-items: center; gap: 17px;
    color: var(--white); font-weight: 500; font-size: 22px; letter-spacing: 1.3px;
    height: 42px;
  }
  .benefits li.two-line { height: 68px; margin-top: 4px; line-height: 1.2; }
  .tick { width: 26px; height: 26px; flex: none; }

  .contact { position: absolute; left: 24px; top: 1546px; width: 516px; }
  .contact-row { display: flex; align-items: center; gap: 16px; color: var(--ink); }
  .contact-row .icon { width: 32px; height: 32px; flex: none; }
  .contact-row--phone { font-weight: 700; font-size: 29px; letter-spacing: 1px; height: 42px; }
  .contact-row--web { font-weight: 500; font-size: 21px; letter-spacing: 1.2px; height: 46px; }
  .contact-row--web b { font-weight: 700; }
  .contact-rule { height: 1.5px; background: var(--ink); opacity: .6; margin: 6px 0 10px; }
  .contact-row--post { font-weight: 500; font-size: 21px; letter-spacing: .8px; height: 40px; }
</style>
</head>
<body>
<div class="banner-frame">
  <div class="banner">
    <svg class="banner-shapes" viewBox="0 0 725 1757" xmlns="http://www.w3.org/2000/svg">
      <defs>
        <linearGradient id="paper" x1="0" y1="0" x2="1" y2="1">
          <stop offset="0" stop-color="#f7fbfc"/>
          <stop offset=".6" stop-color="#ffffff"/>
          <stop offset="1" stop-color="#dcecee"/>
        </linearGradient>
        <linearGradient id="officeScene" x1="0" y1="0" x2="1" y2="1">
          <stop offset="0" stop-color="#e8e6e2"/>
          <stop offset=".45" stop-color="#8a6c7a"/>
          <stop offset=".75" stop-color="#c79d6a"/>
          <stop offset="1" stop-color="#3a3a44"/>
        </linearGradient>
        <linearGradient id="portraitA" x1="0" y1="0" x2="0" y2="1">
          <stop offset="0" stop-color="#eae5dc"/><stop offset=".6" stop-color="#6e90b8"/><stop offset="1" stop-color="#c8a57c"/>
        </linearGradient>
        <linearGradient id="portraitB" x1="0" y1="0" x2="0" y2="1">
          <stop offset="0" stop-color="#eef1f3"/><stop offset=".6" stop-color="#5a7a3a"/><stop offset="1" stop-color="#3a3c40"/>
        </linearGradient>
        <linearGradient id="portraitC" x1="0" y1="0" x2="0" y2="1">
          <stop offset="0" stop-color="#e8e8e4"/><stop offset=".6" stop-color="#f4f4f6"/><stop offset="1" stop-color="#2c2d33"/>
        </linearGradient>
      </defs>

      <rect width="725" height="1757" fill="url(#paper)"/>

      <!-- hero photo area -->
      <path role="img" aria-label="Photo: three colleagues smiling around a desk with laptops in a bright office"
            d="M0,290 C200,292 420,270 600,252 Q675,246 725,320 L725,760 L0,850 Z" fill="url(#officeScene)"/>
      <path d="M0,245 Q55,280 85,295" stroke="#2a2a35" stroke-width="3" fill="none"/>
      <path d="M170,296 Q400,272 600,246 Q675,238 725,305 L725,332 Q672,262 600,268 Q400,290 170,300 Z" fill="var(--teal)"/>
      <path d="M370,268 Q520,242 600,228 Q675,218 725,278 L725,300 Q675,242 600,250 Q500,262 370,272 Z" fill="var(--magenta)"/>

      <!-- magenta band behind portraits -->
      <path d="M0,830 Q300,800 725,745 L725,930 Q690,990 600,998 L0,1000 Z" fill="var(--magenta)"/>
      <path d="M0,880 Q30,830 120,815 L0,830 Z" fill="#c4467f"/>

      <!-- teal information panel -->
      <path d="M0,1010 Q40,970 180,985 L590,1000 Q690,996 725,935 L725,1430 Q650,1530 560,1500 L240,1430 Q80,1410 0,1490 Z" fill="var(--teal)"/>
      <path d="M350,1455 L600,1490 Q680,1495 725,1418 L725,1445 Q680,1520 600,1515 L350,1462 Z" fill="var(--magenta)"/>

      <!-- portraits -->
      <circle role="img" aria-label="Photo: woman in a wheelchair working at a laptop" cx="129" cy="877" r="106" fill="url(#portraitA)" stroke="#ffffff" stroke-width="5"/>
      <circle role="img" aria-label="Photo: woman in a wheelchair smiling with a laptop on her lap" cx="361" cy="877" r="106" fill="url(#portraitB)" stroke="#ffffff" stroke-width="5"/>
      <circle role="img" aria-label="Photo: man in a wheelchair in a shirt and tie holding a phone" cx="592" cy="877" r="106" fill="url(#portraitC)" stroke="#ffffff" stroke-width="5"/>

      <!-- partner badge -->
      <circle cx="634" cy="1617" r="66" fill="#5b2a84" stroke="#ffffff" stroke-width="5"/>
    </svg>

    <div class="brand">
      <span class="brand-mark"></span>
      <div class="brand-name">HARBOUR<br>Plan Partners</div>
    </div>
    <div class="brand-divider"></div>
    <div class="headline">
      <div><span>YOUR</span> PLAN</div>
      <div><span>YOUR</span> WAY</div>
    </div>

    <div class="pill pill--coverage">Australia wide plan management</div>

    <ul class="benefits">
      <li><svg class="tick" viewBox="0 0 26 26"><circle cx="13" cy="13" r="12" fill="#fff"/><circle cx="13" cy="13" r="8.5" fill="none" stroke="#b1306d" stroke-width="1.8"/><path d="M9.3,13.2 L12,15.8 L16.8,10.6" fill="none" stroke="#b1306d" stroke-width="1.8" stroke-linecap="round" stroke-linejoin="round"/></svg>Invoices processed daily</li>
      <li><svg class="tick" viewBox="0 0 26 26"><circle cx="13" cy="13" r="12" fill="#fff"/><circle cx="13" cy="13" r="8.5" fill="none" stroke="#b1306d" stroke-width="1.8"/><path d="M9.3,13.2 L12,15.8 L16.8,10.6" fill="none" stroke="#b1306d" stroke-width="1.8" stroke-linecap="round" stroke-linejoin="round"/></svg>Providers paid within 3 business days</li>
      <li><svg class="tick" viewBox="0 0 26 26"><circle cx="13" cy="13" r="12" fill="#fff"/><circle cx="13" cy="13" r="8.5" fill="none" stroke="#b1306d" stroke-width="1.8"/><path d="M9.3,13.2 L12,15.8 L16.8,10.6" fill="none" stroke="#b1306d" stroke-width="1.8" stroke-linecap="round" stroke-linejoin="round"/></svg>Expense reimbursements</li>
      <li><svg class="tick" viewBox="0 0 26 26"><circle cx="13" cy="13" r="12" fill="#fff"/><circle cx="13" cy="13" r="8.5" fill="none" stroke="#b1306d" stroke-width="1.8"/><path d="M9.3,13.2 L12,15.8 L16.8,10.6" fill="none" stroke="#b1306d" stroke-width="1.8" stroke-linecap="round" stroke-linejoin="round"/></svg>Real time funding access</li>
      <li><svg class="tick" viewBox="0 0 26 26"><circle cx="13" cy="13" r="12" fill="#fff"/><circle cx="13" cy="13" r="8.5" fill="none" stroke="#b1306d" stroke-width="1.8"/><path d="M9.3,13.2 L12,15.8 L16.8,10.6" fill="none" stroke="#b1306d" stroke-width="1.8" stroke-linecap="round" stroke-linejoin="round"/></svg>Your own personal dedicated plan manager</li>
      <li><svg class="tick" viewBox="0 0 26 26"><circle cx="13" cy="13" r="12" fill="#fff"/><circle cx="13" cy="13" r="8.5" fill="none" stroke="#b1306d" stroke-width="1.8"/><path d="M9.3,13.2 L12,15.8 L16.8,10.6" fill="none" stroke="#b1306d" stroke-width="1.8" stroke-linecap="round" stroke-linejoin="round"/></svg>Monthly statements</li>
      <li class="two-line"><svg class="tick" viewBox="0 0 26 26"><circle cx="13" cy="13" r="12" fill="#fff"/><circle cx="13" cy="13" r="8.5" fill="none" stroke="#b1306d" stroke-width="1.8"/><path d="M9.3,13.2 L12,15.8 L16.8,10.6" fill="none" stroke="#b1306d" stroke-width="1.8" stroke-linecap="round" stroke-linejoin="round"/></svg><span>Choice and control<br>(Use both registered and unregistered providers)</span></li>
    </ul>

    <div class="pill pill--contact">Contact Us</div>

    <div class="contact">
      <div class="contact-row contact-row--phone">
        <svg class="icon" viewBox="0 0 32 32"><circle cx="16" cy="16" r="16" fill="#12837f"/><path d="M11.5,8.5 L14,8.5 L15.2,12 L13.6,13.4 Q15,16.8 18.6,18.4 L20,16.8 L23.5,18 L23.5,20.5 Q23,23.5 20,23.3 Q10.5,22 8.7,12 Q8.6,9 11.5,8.5 Z" fill="none" stroke="#fff" stroke-width="1.5" stroke-linejoin="round"/></svg>
        1300 555 019
      </div>
      <div class="contact-row contact-row--web">
        <svg class="icon" viewBox="0 0 32 32"><circle cx="16" cy="16" r="16" fill="#12837f"/><g fill="none" stroke="#fff" stroke-width="1.4"><circle cx="16" cy="16" r="8"/><ellipse cx="16" cy="16" rx="3.6" ry="8"/><path d="M8,16 H24 M9.2,12 H22.8 M9.2,20 H22.8"/></g></svg>
        <span>www.<b>harbourplanpartners</b>.com.au</span>
      </div>
      <div class="contact-rule"></div>
      <div class="contact-row contact-row--post">
        <svg class="icon" viewBox="0 0 32 32"><circle cx="16" cy="16" r="16" fill="#12837f"/><path d="M16,25 Q9.5,17.5 9.5,13.5 A6.5,6.5 0 0 1 22.5,13.5 Q22.5,17.5 16,25 Z" fill="none" stroke="#fff" stroke-width="1.5"/><circle cx="16" cy="13.5" r="2.4" fill="none" stroke="#fff" stroke-width="1.5"/></svg>
        PO Box 4810, Riverbend&nbsp; NSW 2400
      </div>
    </div>
  </div>
</div>
</body>
</html>
```